Wedding Invitations

We are a printing company "inkmorrow" and require multiple wedding invitation designs for our customers in store and online. We would like the designs to be editable in Photoshop if possible, if not then a layout with suggested fonts would be the next best option. We are open to suggestions on design but would like to stick to the general wedding themes some with a modern and some with a classical feel

Industry/Entity Type

Printing

```html
<!DOCTYPE html>
<html lang="en">
<head>
<meta charset="utf-8">
<title>Malcolm &amp; Eloise — Wedding Invitation</title>
<link rel="stylesheet" href="https://fonts.googleapis.com/css2?family=Alfa+Slab+One&family=Comfortaa:wght@300;400&family=Playfair+Display+SC:wght@900&family=Playfair+Display:ital,wght@1,400;1,700&family=Raleway:wght@300;400;600&display=swap">
<style>
  :root {
    --ink: #111111;
    --paper: #ffffff;
    --ribbon: #151515;
    --ribbon-panel: #2c2c2c;
  }
  html, body {
    margin: 0;
    padding: 0;
    width: 1200px;
    height: 2545px;
    overflow: hidden;
    background: var(--paper);
  }
  .invitation {
    display: block;
    width: 1200px;
    height: 2545px;
  }
  .invitation text { fill: var(--ink); }
  .name-bold { font-family: "Playfair Display SC", serif; font-weight: 900; }
  .name-thin { font-family: "Raleway", sans-serif; font-weight: 300; }
  .connector { font-family: "Raleway", sans-serif; font-weight: 400; }
  .rounded { font-family: "Comfortaa", sans-serif; font-weight: 300; }
  .ampersand { font-family: "Playfair Display", serif; font-weight: 700; font-style: italic; }
  .script { font-family: "Playfair Display", serif; font-style: italic; font-weight: 400; }
  .slab { font-family: "Alfa Slab One", serif; }
  .rule { stroke: var(--ink); stroke-width: 0.6; }
  .ribbon { fill: var(--ribbon); }
  .ribbon-panel { fill: var(--ribbon-panel); }
  .invitation .ribbon-text { fill: var(--paper); }
</style>
</head>
<body>
<svg class="invitation" viewBox="0 0 300 636" xmlns="http://www.w3.org/2000/svg" role="img" aria-label="Wedding invitation for Malcolm Westbrooke and Eloise Ashcroft">
  <!-- Couple names -->
  <text class="name-bold" x="28" y="60" font-size="37" textLength="214" lengthAdjust="spacingAndGlyphs">MALCOLM</text>
  <text class="name-thin" x="28" y="88" font-size="29" textLength="244" lengthAdjust="spacingAndGlyphs">WESTBROOKE</text>
  <text class="ampersand" x="150" y="105" font-size="12" text-anchor="middle">&amp;</text>
  <text class="name-bold" x="28" y="140" font-size="37" textLength="210" lengthAdjust="spacingAndGlyphs">ELOISE</text>
  <text class="name-thin" x="28" y="172" font-size="32" textLength="242" lengthAdjust="spacingAndGlyphs">ASHCROFT</text>

  <!-- Parents -->
  <line class="rule" x1="28" y1="184" x2="116" y2="184"/>
  <text class="connector" x="150" y="188" font-size="11" text-anchor="middle">as well as</text>
  <line class="rule" x1="184" y1="184" x2="272" y2="184"/>
  <text class="rounded" x="36" y="216" font-size="22" textLength="226" lengthAdjust="spacingAndGlyphs">parker <tspan class="ampersand" font-style="normal">&amp;</tspan> hayes</text>
  <line class="rule" x1="28" y1="226" x2="114" y2="226"/>
  <text class="connector" x="150" y="230" font-size="11" text-anchor="middle">have chosen</text>
  <line class="rule" x1="186" y1="226" x2="272" y2="226"/>

  <!-- Date -->
  <text class="name-bold" x="30" y="258" font-size="23" textLength="236" lengthAdjust="spacingAndGlyphs">SEPTEMBER 20th</text>
  <text class="script" x="68" y="271" font-size="13" textLength="194" lengthAdjust="spacingAndGlyphs">two thousand and fourteen</text>

  <!-- Ribbon: as the first -->
  <g class="banner">
    <path class="ribbon" d="M30 282 H270 L262 292.5 L270 303 H30 L38 292.5 Z"/>
    <rect class="ribbon-panel" x="70" y="284" width="160" height="17"/>
    <text class="slab ribbon-text" x="150" y="298" font-size="14" text-anchor="middle" letter-spacing="0.6">AS THE FIRST</text>
  </g>
  <text class="script" x="150" y="317" font-size="10" text-anchor="middle">day of the rest</text>
  <text class="name-thin" x="40" y="343" font-size="29" textLength="226" lengthAdjust="spacingAndGlyphs">of their lives</text>
  <text class="slab" x="30" y="377" font-size="30" textLength="240" lengthAdjust="spacingAndGlyphs">TOGETHER</text>
  <text class="connector" x="33" y="399" font-size="11" textLength="235" lengthAdjust="spacingAndGlyphs">you are invited to share in their joy</text>

  <!-- As they tie the knot -->
  <g class="tie-the-knot">
    <text class="name-thin" x="29" y="420" font-size="19" textLength="22" lengthAdjust="spacingAndGlyphs">AS</text>
    <text class="connector" x="30" y="428" font-size="6" textLength="18" lengthAdjust="spacingAndGlyphs">THEY</text>
    <line class="rule" x1="56" y1="405" x2="82" y2="405"/>
    <line class="rule" x1="56" y1="428" x2="82" y2="428"/>
    <text class="slab" x="84" y="428" font-size="29" textLength="68" lengthAdjust="spacingAndGlyphs">TIE</text>
    <text class="connector" x="159" y="412" font-size="6.5" text-anchor="middle">T</text>
    <text class="connector" x="159" y="419" font-size="6.5" text-anchor="middle">H</text>
    <text class="connector" x="159" y="426" font-size="6.5" text-anchor="middle">E</text>
    <text class="slab" x="167" y="428" font-size="29" textLength="103" lengthAdjust="spacingAndGlyphs">KNOT</text>
  </g>

  <!-- Time -->
  <line class="rule" x1="28" y1="437" x2="272" y2="437"/>
  <text x="30" y="460" font-size="22" textLength="240" lengthAdjust="spacingAndGlyphs"><tspan class="slab">THREE</tspan><tspan class="name-thin">THIRTY</tspan><tspan class="slab">PM</tspan></text>
  <line class="rule" x1="28" y1="466" x2="272" y2="466"/>

  <!-- Venue ribbon -->
  <g class="banner">
    <path class="ribbon" d="M30 473 H270 L262 482 L270 491 H30 L38 482 Z"/>
    <rect class="ribbon-panel" x="74" y="474.5" width="152" height="15"/>
    <text class="slab ribbon-text" x="150" y="487" font-size="11" text-anchor="middle" letter-spacing="0.6">THE SILVERPINE</text>
  </g>
  <text class="script" x="150" y="505" font-size="11" text-anchor="middle">hotel</text>
  <text class="name-thin" x="30" y="525" font-size="20" textLength="238" lengthAdjust="spacingAndGlyphs">in the garden &amp; courtyard</text>
  <text class="slab" x="30" y="548" font-size="13.5" textLength="238" lengthAdjust="spacingAndGlyphs">12 - 18 WILLOW RD ASHFORD</text>
  <line class="rule" x1="28" y1="553" x2="272" y2="553"/>

  <!-- RSVP -->
  <text class="connector" x="30" y="567" font-size="11" textLength="238" lengthAdjust="spacingAndGlyphs">RSVP BY JULY 30TH TO MAL OR ELOISE</text>
  <line class="rule" x1="28" y1="577" x2="70" y2="577"/>
  <text class="connector" x="150" y="580" font-size="6.5" font-weight="600" text-anchor="middle" textLength="150" lengthAdjust="spacingAndGlyphs">ON 0400 123 456 <tspan class="slab">OR</tspan> 0400 765 432</text>
  <line class="rule" x1="230" y1="577" x2="272" y2="577"/>
</svg>
</body>
</html>
```